Pet and Potrait photography business needs web site design

I need a web design that is for a portrait and pet photography business based in Tasmania, Australia. It is a small, simple concept, photography business that focuses on portraits and pet photography only. I need something that is clean, maybe a white background, fun, and appealing to families. The design must make my images stand out and be the focus. The final design needs to show that it is aimed a families, pet owners, and is all about the clients - albeit the two or four legged kinds.

Business name is: maple lantern photography

I need it to be able to have the following:

- Include space for logo design which is also through SketchPlaza
- Home Page which has a gallery of my images (which you can click an arrow - either forward or back - that showcases my images
- About Page
- Portfolio Page (preferably two a) for portraits, and b) for pet photography
- Pricing page
- secure log in client page
- Contact page
Updates

Reason: Waiting for logo design to be completed to fit in with overall website design.

Target Market(s)

Families
Pet owners
Single couples who have fur babies

Industry/Entity Type

Business

Font styles to use
Serif
Decorative
Script

Colors

Designer to choose colors to be used in the design.

Requirements
Must have
• the website must provide the ability for me to upload and change images regularly.
Nice to have
• Logo design is a secondary project that will need to be worked on as well. I will pay an additional amount for those that are prepared to include this in the project.
Should not have
• No graffiti style writing.
It has to be elegant, and stylish and be aimed at females.
Women are going to be the driver for having portraits done of either their babies, children, or fur babies - i.e. pets.

```html
<!DOCTYPE html>
<html lang="en">
<head>
<meta charset="utf-8">
<title>Maple Lantern Photography</title>
<link rel="stylesheet" href="https://fonts.googleapis.com/css2?family=Questrial&family=Oswald:wght@300;400&family=Lato:wght@400;700&display=swap">
<style>
  :root {
    --header-bg: #161616;
    --header-line: #262626;
    --page-bg: #ececec;
    --panel-bg: #ffffff;
    --panel-border: #d6d6d6;
    --accent: #00b4e8;
    --accent-deep: #0a9dd0;
    --tile-dark-top: #4b4d50;
    --tile-dark-bottom: #030303;
    --footer-bg: #141414;
    --text-light: #ffffff;
    --icon-bg: #f3f3f3;
    --icon-ink: #3b5f9a;
  }
  * { box-sizing: border-box; margin: 0; padding: 0; }
  html, body { width: 1200px; height: 956px; overflow: hidden; }
  body {
    position: relative;
    background: var(--page-bg);
    font-family: "Lato", sans-serif;
  }

  .site-header {
    position: absolute; left: 0; top: 0; width: 1200px; height: 214px;
    background: var(--header-bg);
    border-bottom: 3px solid var(--header-line);
  }
  .brand {
    position: absolute; left: 82px; top: 62px;
    font-family: "Questrial", sans-serif;
    color: var(--text-light);
    font-size: 40px; line-height: 44px;
    letter-spacing: 0.5px;
  }
  .main-nav {
    position: absolute; left: 519px; top: 119px;
    display: flex; align-items: center; height: 42px;
  }
  .main-nav a {
    font-family: "Questrial", sans-serif;
    font-size: 17px; color: var(--text-light);
    text-decoration: none; text-transform: uppercase;
    height: 42px; line-height: 42px;
  }
  .main-nav a.is-active {
    background: var(--accent); border-radius: 21px;
    width: 94px; text-align: center;
  }
  .nav-about { margin-left: 16px; }
  .nav-portfolio { margin-left: 38px; }
  .nav-pricing { margin-left: 38px; }
  .nav-login { margin-left: 38px; }
  .nav-contact { margin-left: 38px; }

  .showcase {
    position: absolute; left: 61px; top: 231px; width: 1071px; height: 621px;
    background: var(--panel-bg);
    border: 1px solid var(--panel-border);
  }
  .category-list {
    position: absolute; left: 0; top: 0; width: 220px; height: 619px;
    list-style: none;
  }
  .category {
    height: 155px;
    padding: 52px 0 0 30px;
    background: linear-gradient(var(--accent), var(--accent-deep));
    border-bottom: 1px solid #0a8fbf;
    color: var(--text-light);
  }
  .category:last-child { height: 154px; border-bottom: none; }
  .category.is-current {
    background: linear-gradient(var(--tile-dark-top), var(--tile-dark-bottom));
    border-bottom: 1px solid #000;
  }
  .category-title {
    font-family: "Oswald", sans-serif; font-weight: 300;
    font-size: 28px; line-height: 30px; text-transform: uppercase;
  }
  .category-note { font-size: 15px; line-height: 18px; }

  .featured-photo {
    position: absolute; left: 257px; top: 37px; width: 776px; height: 546px;
    background: radial-gradient(ellipse at 50% 60%, #f2cdb4 0%, #d8ad86 40%, #c99b6e 75%, #b88b60 100%);
  }

  .site-footer {
    position: absolute; left: 0; top: 885px; width: 1200px; height: 71px;
    background: var(--footer-bg);
    border-top: 3px solid #2a2a2a;
  }
  .legal {
    position: absolute; left: 83px; top: 30px;
    font-size: 15px; color: var(--text-light);
    text-transform: uppercase;
  }
  .social-links {
    position: absolute; left: 964px; top: 22px;
    display: flex; gap: 8px;
  }
  .social-links span {
    width: 34px; height: 34px; border-radius: 50%;
    background: var(--icon-bg);
    border: 2px solid #cfcfcf;
  }
</style>
</head>
<body>
  <header class="site-header">
    <div class="brand">maple lantern<br>photography</div>
    <nav class="main-nav">
      <a class="is-active" href="#">Home</a>
      <a class="nav-about" href="#">About</a>
      <a class="nav-portfolio" href="#">Portfolio</a>
      <a class="nav-pricing" href="#">Pricing</a>
      <a class="nav-login" href="#">Log In</a>
      <a class="nav-contact" href="#">Contact</a>
    </nav>
  </header>

  <main class="showcase">
    <ul class="category-list">
      <li class="category is-current">
        <div class="category-title">Portrait</div>
        <div class="category-note">Your Sweet Kids</div>
      </li>
      <li class="category">
        <div class="category-title">Pet</div>
        <div class="category-note">Photo of Your Fur Babies</div>
      </li>
      <li class="category">
        <div class="category-title">Photo</div>
        <div class="category-note">Best Photo of the Month</div>
      </li>
      <li class="category">
        <div class="category-title">Latest</div>
        <div class="category-note">Just Taken Shots</div>
      </li>
    </ul>
    <div class="featured-photo" role="img" aria-label="Featured photograph: two young sisters hugging on a sandy beach"></div>
  </main>

  <footer class="site-footer">
    <p class="legal">© 2013, All Rights Reserved, Privacy Policy</p>
    <div class="social-links" aria-label="Social links">
      <span></span><span></span><span></span><span></span>
    </div>
  </footer>
</body>
</html>
```